Verpackungsdesign für Räucherstäbchen
Zielgruppe
Unsere Firma Lindenkram importiert hochwertige und reine Räucherstoffe aus entfernten Ländern. Dabei steht die Nachhaltigkeit und der faire Handel im Vordergrund. Unser Fokus ist dabei der Handel mit Weihrauch, den wir aus den Ursprungsländern importieren und an Großhändler, Händler und Endkunden weiterverkaufen. Seit einigen Jahren haben wir den Wunsch echte, natürliche Räucherstäbchen auf den Markt zu bringen. Dieses Projekt wurde nun umgesetzt.
Wir suchen ein Verpackungsdesign für unsere Räucherstäbchen. Die Räucherstäbchen sind absolut naturrein (95% aller Räucherstäbchen auf dem Markt sind es nicht), ohne Chemie, ohne Parfum, ohne Synthetik. Absolut rein, hergestellt aus besten Rohstoffen, teilweise direkt aus Deutschland.
Aufgabenstellung
Da die Räucherstäbchen auch in den Handel kommen werden, ist es am Besten, dass die Verpackung eine Faltschachtel ist mit den Maßen: 6cm Breite, 22cm Länge, 1,5cm Höhe
Die Schachtel sollte sehr natürlich ausschauen und die Farben nicht zu kräftig.
Es wird ein Logo darauf geben, das ich hochladen werde.
Farben sollten natürlich sein, Elegant und natürlich. Wir wissen nicht genau, wie die Verpackung aussehen soll, doch sicher ist, dass sie nicht zu überladen sein sollte. Die Verpackung sollte schlicht, natürlich und edel sein
Wir planen über 20 Sorten: Harze, Sandelholz, Patchouli etc.
Das Design der Verpackung sollte das berücksichtigen. Ein Design, das später an die verschiedenen Sorten angepasst werden kann
Für das Beispiel-Design:
Text auf der Vorderseite:
Räucherstäbchen
Weihrauch Afrika
Made with love in Germany
Natur pur
Rückseite:
Naturreine Räucherstäbchen hergestellt mit den reinsten Rohstoffen
Ohne chemische oder synthetische Zusätze, kein Parfum, keine Abbrennhilfe
Brenndauer: ca. 45- 60min
Eine Verpackung beinhaltet 10 Räucherstäbchen.
Hergestellt von:
Made by
Lindenkram
Birkenauer Weg 14
64711 Erbachtal

```html
<!DOCTYPE html>
<html lang="de">
<head>
<meta charset="utf-8">
<title>Räucherstäbchen – Faltschachtel Weihrauch Afrika</title>
<link rel="stylesheet" href="https://fonts.googleapis.com/css2?family=Alegreya:wght@400;500&family=Alegreya+Sans:wght@400;500;700&display=swap">
<style>
  :root {
    --stage: #0d0b09;
    --carton: #ddb766;
    --carton-light: #e3c077;
    --bark: #8a4a1f;
    --ink: #8d4c1e;
    --ink-soft: #9a5b2a;
    --pattern-dark: #9a5424;
    --pattern-mid: #b06d32;
    --pattern-light: #c48a45;
    --fold: #c89d4e;
    --cut-seam: #e0449a;
    --leaf: #4f8a76;
  }
  * { margin: 0; padding: 0; box-sizing: border-box; }
  html, body { width: 1200px; height: 848px; overflow: hidden; background: var(--stage); }
  .stage { position: relative; width: 1200px; height: 848px; }

  .dieline {
    position: absolute;
    left: 356px; top: 16px;
    width: 425px; height: 710px;
    transform: scale(1.15);
    transform-origin: 0 0;
  }
  .dieline > * { position: absolute; }

  .flap { background: var(--carton); }
  .flap--top { left: 215px; top: 0; width: 168px; height: 44px; }
  .flap--bottom { left: 215px; top: 666px; width: 168px; height: 44px; }
  .body-panel { left: 0; top: 43px; width: 425px; height: 624px; background: var(--carton); }

  .fold { top: 43px; width: 1px; height: 624px; background: var(--fold); }
  .fold--glue { left: 170px; background: var(--cut-seam); }
  .fold--a { left: 215px; }
  .fold--b { left: 383px; }

  .label-natur {
    left: 232px; top: 0; width: 133px; height: 95px;
    background: var(--bark);
    color: var(--carton-light);
    font: 400 15px/1 "Alegreya", serif;
    display: flex; align-items: flex-end; justify-content: center;
    padding-bottom: 10px;
  }

  .pattern-band {
    left: 0; width: 425px;
    background: linear-gradient(180deg, var(--pattern-mid), var(--pattern-dark) 50%, var(--pattern-mid));
  }
  .pattern-band--main { top: 200px; height: 176px; }
  .pattern-band--lower { top: 432px; height: 61px; }

  .emblem {
    left: 291px; top: 123px; width: 16px; height: 16px;
    border-radius: 50%;
    background: var(--pattern-light);
  }

  .front-title {
    left: 215px; width: 168px; text-align: center;
    font-family: "Alegreya", serif; font-weight: 400;
    color: var(--ink); letter-spacing: .02em; line-height: 1;
  }
  .front-title--product { top: 162px; font-size: 14px; }
  .front-title--variety { top: 396px; font-size: 13.5px; }
  .back-variety { left: 12px; top: 396px; font: 400 13.5px/1 "Alegreya", serif; color: var(--ink); letter-spacing: .02em; }

  .tagline { left: 215px; width: 168px; top: 508px; text-align: center; font: 500 10px/1 "Alegreya Sans", sans-serif; color: var(--ink); }

  .brand { left: 215px; width: 168px; top: 552px; display: flex; flex-direction: column; align-items: center; }
  .brand__disc { width: 58px; height: 58px; border-radius: 50%; border: 1px solid var(--leaf); }
  .brand__name { margin-top: 7px; font: 700 10.5px/1 "Alegreya Sans", sans-serif; color: var(--leaf); }
  .brand__claim { margin-top: 2px; font: 700 7px/1 "Alegreya Sans", sans-serif; color: var(--leaf); }

  .back-copy { left: 20px; width: 130px; font: 400 7.5px/1.38 "Alegreya Sans", sans-serif; color: var(--ink-soft); }
  .back-copy strong { font-weight: 700; }
  .back-copy--intro { top: 100px; }
  .back-copy--burn { top: 164px; }
  .back-copy--content { top: 507px; }
  .back-copy--maker { top: 581px; }
  .back-copy--maker p + p { margin-top: 13px; }
</style>
</head>
<body>
<main class="stage">
  <section class="dieline" aria-label="Faltschachtel Räucherstäbchen, abgewickelt">
    <div class="flap flap--top"></div>
    <div class="body-panel"></div>
    <div class="flap flap--bottom"></div>

    <div class="pattern-band pattern-band--main" role="img" aria-label="Ornamentband mit Blütenmuster in Brauntönen"></div>
    <div class="pattern-band pattern-band--lower" role="img" aria-label="Schmales Ornamentband mit Blütenmuster in Brauntönen"></div>

    <span class="fold fold--glue"></span>
    <span class="fold fold--a"></span>
    <span class="fold fold--b"></span>

    <div class="label-natur">Natur pur</div>

    <div class="emblem" role="img" aria-label="Kleines Blütenornament"></div>

    <h1 class="front-title front-title--product">RÄUCHERSTÄBCHEN</h1>
    <div class="back-copy back-copy--intro">Naturreine Räucherstäbchen hergestellt mit den reinsten Rohstoffen. Ohne chemische oder synthetische Zusätze, kein Parfum, keine Abbrennhilfe.</div>
    <div class="back-copy back-copy--burn"><strong>Brenndauer:</strong> ca. 45- 60min</div>

    <div class="back-variety">WEIHRAUCH AFRIKA</div>
    <h2 class="front-title front-title--variety">WEIHRAUCH AFRIKA</h2>

    <p class="tagline">Made with love in Germany</p>
    <div class="back-copy back-copy--content">Eine Verpackung beinhaltet<br><strong>10 Räucherstäbchen.</strong></div>
    <div class="back-copy back-copy--maker">
      <p><strong>Hergestellt von:</strong></p>
      <p>Made by<br>Lindenkram<br>Birkenauer Weg 14<br>64711 Erbachtal</p>
    </div>

    <div class="brand">
      <span class="brand__disc"></span>
      <span class="brand__name">lindenkram-shop.de</span>
      <span class="brand__claim">pure resins, woods &amp; more</span>
    </div>
  </section>
</main>
</body>
</html>
```